Need Help having my business card stand out

I am the owner of Pine Ridge Canine Coaching and would like for my business cards to stand out. I have been trying to keep designing them myself but I can't get what I have in my head on the card. I will try my best to post templates that I like for inspirations. I want something unique but elegant. I don't want in to look cartoony or cheesy. It needs to pop in a pet shop but also in a coffee shop or gym.

Target Market(s)

Dog owners, Married ,No young kids Jr High school kids and up (maybe kids on the way) Executives, Stay at home moms/wives, Small business owners

Industry/Entity Type

Dog Training

Contact Information for Business Card

Trevor Holloway, 555-304-7162, info@pineridgecanine.example, www.pineridgecanine.example

Colors

Designer to choose colors to be used in the design.

Requirements
Must have
• my logo
Should not have
• Cursive lettering

```html
<!DOCTYPE html>
<html lang="en">
<head>
<meta charset="utf-8">
<title>Pine Ridge Canine Coaching – Business Card</title>
<link href="https://fonts.googleapis.com/css2?family=Josefin+Sans:wght@300;400&display=swap" rel="stylesheet">
<style>
  :root {
    --backdrop: #dcd3d3;
    --card: #f6f6f6;
    --pattern: #e4e4e4;
    --ink: #7a7a7a;
    --ink-dark: #666666;
    --rule: #8d8d8d;
    --accent: #b08a3e;
    --label: #8a8585;
  }
  * { margin: 0; padding: 0; box-sizing: border-box; }
  html, body { width: 1200px; height: 1200px; overflow: hidden; }
  body {
    background: var(--backdrop);
    font-family: "Josefin Sans", sans-serif;
    font-weight: 300;
    position: relative;
  }
  .side-label {
    position: absolute;
    right: 718px;
    font-size: 42px;
    font-weight: 300;
    color: var(--label);
    letter-spacing: 1px;
    line-height: 1;
  }
  .side-label--back { top: 500px; }
  .side-label--front { top: 912px; }

  .card {
    position: absolute;
    left: 506px;
    width: 630px;
    height: 378px;
    background: var(--card);
    overflow: hidden;
  }
  .card--back { top: 344px; }
  .card--front { top: 742px; }

  .pattern-band {
    position: absolute;
    left: 0; right: 0;
    height: 64px;
    background: var(--pattern);
  }
  .pattern-band--top { top: 0; }
  .pattern-band--bottom { bottom: 0; height: 60px; }

  .rule {
    position: absolute;
    left: 45px; right: 45px;
    height: 1.5px;
    background: var(--rule);
  }

  /* Back */
  .brand-mark {
    position: absolute;
    left: 45px; right: 45px;
    top: 72px; height: 238px;
    display: flex;
    flex-direction: column;
    align-items: center;
    justify-content: center;
    gap: 18px;
  }
  .brand-mark__dot {
    width: 54px; height: 54px;
    border-radius: 50%;
    background: var(--ink);
  }
  .brand-mark__name {
    font-size: 30px;
    font-weight: 400;
    color: var(--ink);
    letter-spacing: 2px;
    text-align: center;
    line-height: 1.2;
  }

  /* Front */
  .holder-name {
    position: absolute;
    left: 0; right: 0; top: 100px;
    text-align: center;
    font-size: 30px;
    font-weight: 300;
    letter-spacing: 4px;
    color: var(--ink-dark);
  }
  .holder-name__rule {
    position: absolute;
    left: 294px; width: 42px; top: 148px;
    height: 1.5px;
    background: var(--rule);
  }
  .holder-role {
    position: absolute;
    left: 0; right: 0; top: 157px;
    text-align: center;
    font-size: 13px;
    letter-spacing: 1px;
    color: var(--ink);
  }
  .holder-brand {
    position: absolute;
    left: 0; right: 0; top: 188px;
    text-align: center;
    font-size: 13px;
    font-weight: 400;
    letter-spacing: 1px;
    color: var(--ink);
  }
  .contact {
    position: absolute;
    display: flex;
    align-items: center;
    gap: 10px;
    font-size: 14px;
    color: var(--ink);
  }
  .contact svg { width: 16px; height: 16px; fill: var(--accent); flex: none; }
</style>
</head>
<body>

  <div class="side-label side-label--back">BACK</div>
  <div class="side-label side-label--front">FRONT</div>

  <section class="card card--back">
    <div class="pattern-band pattern-band--top" role="img" aria-label="Fine dot pattern band"></div>
    <div class="rule" style="top:69px"></div>
    <div class="brand-mark">
      <div class="brand-mark__dot"></div>
      <div class="brand-mark__name">Pine Ridge<br>Canine Coaching</div>
    </div>
    <div class="rule" style="top:309px"></div>
    <div class="pattern-band pattern-band--bottom" role="img" aria-label="Fine dot pattern band"></div>
  </section>

  <section class="card card--front">
    <div class="pattern-band pattern-band--top" style="height:70px" role="img" aria-label="Fine dot pattern band"></div>
    <h1 class="holder-name">TREVOR HOLLOWAY</h1>
    <div class="holder-name__rule"></div>
    <p class="holder-role">Founder and Owner of Pine Ridge Canine Coaching</p>
    <p class="holder-brand">Pine Ridge Canine Coaching</p>
    <div class="rule" style="top:222px"></div>

    <div class="contact" style="left:91px; top:244px">
      <svg viewBox="0 0 16 16"><circle cx="8" cy="8" r="7" fill="none" stroke="#b08a3e" stroke-width="2"/><path d="M1 8h14M8 1c-3 3-3 11 0 14M8 1c3 3 3 11 0 14" fill="none" stroke="#b08a3e" stroke-width="1.4"/></svg>
      <span>www.pineridgecanine.example</span>
    </div>
    <div class="contact" style="left:370px; top:244px">
      <svg viewBox="0 0 16 16"><path d="M3.5 1l2.5 3-1.5 2c1 2 3 4 5 5l2-1.5 3 2.5-1.5 2.5C8 15 1 8 1 2.5z"/></svg>
      <span>555-304-7162</span>
    </div>

    <div class="rule" style="top:290px"></div>

    <div class="contact" style="left:91px; top:308px">
      <svg viewBox="0 0 16 16"><path d="M8 0a5.5 5.5 0 0 0-5.5 5.5C2.5 10 8 16 8 16s5.5-6 5.5-10.5A5.5 5.5 0 0 0 8 0zm0 8a2.5 2.5 0 1 1 0-5 2.5 2.5 0 0 1 0 5z"/></svg>
      <span>Maple Springs, Texas 77000</span>
    </div>
    <div class="contact" style="left:370px; top:308px">
      <svg viewBox="0 0 16 16"><path d="M0 3h16v10H0z"/><path d="M0 3l8 6 8-6" fill="none" stroke="#f6f6f6" stroke-width="1.4"/></svg>
      <span>info@pineridgecanine.example</span>
    </div>
  </section>

</body>
</html>
```